Flyer Design for Private Car Service

Flyer should cater to Business Travelers and Executives who travel Business Class or First Class.
Flyer should include images attached.
Flyer should include the below text
Dallas to Austin
Chauffeured SUVs
• Travel Dallas to Austin in a new 2025 Marlow Strider for $499 one-way
• Trip includes a Uniformed Chauffeur who has a Commercial Drivers License (CDL)
• You can Schedule Chauffeur Pickup at Your Home in Dallas
• Our Chauffeur will Drop You Off at Your Final Destination in Austin
• You can Schedule Chauffeur Return Pickup in Austin and Return Back to Dallas.
• We offer Faster Times on Door-to-Door Travel than Bluecrest Airways
• We offer Comparable Prices on Door-to-Door Travel Times than Bluecrest Airways
• All of our trips are insured with $500k of commercial auto insurance
• Our Passengers can Talk on Cell Phone & Conduct Quill calls Throughout Travel
• Our Passengers have Maximum Privacy, Comfort and First-Class Amenities.
• Our Passengers Avoid Harwick Vale Field and KPR Airport hassles & delays
• Member Brenton Chamber of Commerce, Larkmoor Chamber of Commerce.
• Book your trip today at www.ridemarquel.example
Target Market(s)
Business Travelers
Look and feel
Each slider illustrates characteristics of the customer's brand and the style your logo design should communicate.

```html
<!DOCTYPE html>
<html lang="en">
<head>
<meta charset="utf-8">
<title>Dallas to Austin – Chauffeured SUVs</title>
<link rel="stylesheet" href="https://fonts.googleapis.com/css2?family=Bungee&family=Pathway+Gothic+One&family=Hind:wght@400;700&family=Cormorant+Garamond:wght@500&display=swap">
<style>
  :root{
    --bg:#2b2b2b;
    --gold:#f6b400;
    --gold-deep:#f0a800;
    --white:#ffffff;
    --ink:#1d1d1d;
    --photo-a:#6b6b6b;
    --photo-b:#cfcfcf;
  }
  *{margin:0;padding:0;box-sizing:border-box}
  html,body{width:848px;height:1200px;overflow:hidden;background:var(--bg)}
  .flyer{position:relative;width:848px;height:1200px;background:var(--bg);overflow:hidden;color:var(--white);font-family:'Hind',sans-serif}
  .headline{position:absolute;left:48px;top:62px;font-family:'Bungee',sans-serif;color:var(--gold);font-size:68px;line-height:114px;letter-spacing:1px;text-transform:uppercase}
  .subhead{position:absolute;left:46px;top:280px;font-family:'Pathway Gothic One',sans-serif;font-size:92px;line-height:100px;color:var(--white)}
  .brand-tab{position:absolute;left:507px;top:0;width:281px;height:230px;filter:drop-shadow(0 4px 10px rgba(0,0,0,.45))}
  .brand-tab svg{display:block}
  .brand-name{position:absolute;left:507px;top:92px;width:281px;text-align:center;font-family:'Cormorant Garamond',serif;font-weight:500;font-size:36px;letter-spacing:3px;color:var(--ink)}
  .brand-mark{position:absolute;left:637px;top:48px;width:22px;height:22px;border-radius:50%;background:var(--ink)}
  .photos{position:absolute;left:0;top:0}
  .features{position:absolute;left:37px;top:516px;list-style:none;font-size:15.2px;line-height:19.4px;text-transform:uppercase;color:var(--white)}
  .features li{margin-bottom:6.6px}
  .highlights{position:absolute;left:48px;top:1008px;list-style:none;color:var(--gold);font-size:17px;line-height:21.5px;text-transform:uppercase}
  .cta{position:absolute;left:386px;top:1111px;width:300px;text-align:center}
  .cta-lead{font-size:16.5px;line-height:20px;text-transform:uppercase;color:var(--white)}
  .cta-url{font-weight:700;font-size:24.5px;line-height:32px;color:var(--gold);text-transform:uppercase;white-space:nowrap;margin-left:-40px;margin-right:-40px}
</style>
</head>
<body>
<main class="flyer">
  <h1 class="headline">Dallas to<br>Austin</h1>
  <h2 class="subhead">Chauffeured<br>SUVs</h2>

  <div class="brand-tab">
    <svg width="281" height="230" viewBox="0 0 281 230">
      <path d="M0 0 H281 V229 Q140 170 0 229 Z" fill="#ffffff"/>
    </svg>
  </div>
  <span class="brand-mark"></span>
  <div class="brand-name">MARQUEL</div>

  <svg class="photos" width="848" height="1200" viewBox="0 0 848 1200">
    <defs>
      <linearGradient id="tone-a" x1="0" y1="0" x2="1" y2="1">
        <stop offset="0" stop-color="#9a9a9a"/>
        <stop offset="1" stop-color="#2e2e2e"/>
      </linearGradient>
      <linearGradient id="tone-b" x1="0" y1="0" x2="1" y2="1">
        <stop offset="0" stop-color="#8c8f94"/>
        <stop offset="1" stop-color="#262626"/>
      </linearGradient>
      <linearGradient id="tone-c" x1="0" y1="0" x2="0" y2="1">
        <stop offset="0" stop-color="#b9b4b0"/>
        <stop offset="1" stop-color="#d8d3cf"/>
      </linearGradient>
    </defs>
    <polygon role="img" aria-label="Uniformed chauffeur opening an SUV door for a business passenger"
      points="506,415 786,258 786,573" fill="url(#tone-a)" stroke="#ffffff" stroke-width="5" stroke-linejoin="round"/>
    <polygon role="img" aria-label="Two uniformed chauffeurs in caps standing side by side"
      points="496,543 496,852 773,698" fill="url(#tone-b)" stroke="#ffffff" stroke-width="5" stroke-linejoin="round"/>
    <polygon role="img" aria-label="Chauffeurs lined up beside a fleet of new SUVs"
      points="509,959 786,801 786,1114" fill="url(#tone-c)" stroke="#ffffff" stroke-width="5" stroke-linejoin="round"/>
  </svg>

  <ul class="features">
    <li>• Travel Dallas to Austin in a new 2025<br>Marlow Strider for $499 one-way</li>
    <li>• Trip includes a uniformed chauffeur<br>who has a commercial drivers license (CDL)</li>
    <li>• You can schedule chauffeur pickup<br>at your home in Dallas</li>
    <li>• Our chauffeur will drop you off at<br>your final destination in Austin</li>
    <li>• You can schedule chauffeur return<br>pickup in Austin and return back to Dallas.</li>
    <li>• We offer faster times on door-to-door<br>travel than Bluecrest Airways</li>
    <li>• We offer comparable prices on door-to-door<br>travel times than Bluecrest Airways</li>
    <li>• All of our trips are insured with $500K of<br>commercial auto insurance</li>
    <li>• Our passengers can talk on cell phone &amp; conduct<br>Quill calls throughout travel</li>
    <li>• Our passengers have maximum privacy,<br>comfort and first-class amenities.</li>
  </ul>

  <ul class="highlights">
    <li>&gt; Our passengers avoid Harwick Vale Field and KPR<br>Airport hassles &amp; delays</li>
    <li>&gt; Member Brenton Chamber of Commerce,<br>Larkmoor Chamber of Commerce.</li>
  </ul>

  <div class="cta">
    <p class="cta-lead">Book your trip today at</p>
    <p class="cta-url">www.ridemarquel.example</p>
  </div>
</main>
</body>
</html>
```